Modern Label for Loose Tea pouches on 4.5x6 Label

We need a new label for our teas that is very simple in design, but stylish and modern. This will be used to print labels for our loose tea pouches. The label will be at max 4.5x6 inches in size. There should be a place for the tea name, description, ingredients, and size that is changeable.
Preferably an AI file that allows me to setup variables to change the above items. There will also need to be our logo which is supplied, and our address on the label.
Address:
Brevo Leaf
846 Lower Maple Lane
Fernbrook, VT 05617
Target Market(s)
Tea Lovers
Requirements
Must have
- Adobe Illustrator file with variables setup for replacement of tea name, description, ingredients, and size (weights 2oz, 4oz, 8oz, 1lb)

```html
<!DOCTYPE html>
<html lang="en">
<head>
<meta charset="utf-8">
<title>Brevo Leaf – Loose Tea Pouch Label</title>
<link href="https://fonts.googleapis.com/css2?family=Open+Sans:wght@400;700&family=Great+Vibes&display=swap" rel="stylesheet">
<style>
  :root {
    --canvas: #ffffff;
    --magenta: #c93d8b;
    --magenta-deep: #a5206a;
    --lime: #bed62f;
    --lime-light: #e4ee8c;
    --green: #3db54a;
    --ink: #231f20;
    --white: #ffffff;
    --label-text: #3a2a33;
  }
  * { margin: 0; padding: 0; box-sizing: border-box; }
  html, body {
    width: 1200px;
    height: 1200px;
    overflow: hidden;
    background: var(--canvas);
  }
  .canvas {
    position: relative;
    width: 1200px;
    height: 1200px;
  }
  .label {
    position: absolute;
    left: 174px;
    top: 28px;
    width: 853px;
    height: 1136px;
    overflow: hidden;
    font-family: "Open Sans", Arial, sans-serif;
  }
  .label-art {
    position: absolute;
    inset: 0;
    width: 100%;
    height: 100%;
    display: block;
  }
  .brand-name {
    position: absolute;
    left: 0;
    width: 856px;
    top: 580px;
    text-align: center;
    font-family: "Open Sans", Arial, sans-serif;
    font-weight: 700;
    font-size: 74px;
    line-height: 84px;
    letter-spacing: 2px;
    color: var(--lime);
    white-space: nowrap;
  }
  .tea-name {
    position: absolute;
    left: 0;
    width: 856px;
    top: 702px;
    text-align: center;
    font-family: "Great Vibes", cursive;
    font-size: 58px;
    line-height: 76px;
    color: var(--lime-light);
    white-space: nowrap;
  }
  .address-panel {
    position: absolute;
    left: 36px;
    top: 928px;
    width: 278px;
    height: 220px;
    background: var(--ink);
    border-radius: 32px 32px 0 0;
    padding: 38px 0 0 26px;
  }
  .address-brand {
    font-family: "Open Sans", Arial, sans-serif;
    font-weight: 700;
    font-size: 40px;
    line-height: 48px;
    color: var(--lime);
    margin-bottom: 6px;
    white-space: nowrap;
  }
  .address-line {
    padding-left: 4px;
    font-size: 20px;
    line-height: 30px;
    color: var(--white);
    white-space: nowrap;
  }
  .field-label {
    position: absolute;
    left: 529px;
    font-family: Arial, "Open Sans", sans-serif;
    font-size: 14px;
    line-height: 18px;
    letter-spacing: 0.3px;
    color: var(--label-text);
  }
  .field-description { top: 926px; }
  .field-ingredients { top: 1031px; }
</style>
</head>
<body>
<div class="canvas">
  <div class="label">
    <svg class="label-art" viewBox="218 35 1066 1420" preserveAspectRatio="none">
      <defs>
        <linearGradient id="magentaField" x1="0" y1="0" x2="1" y2="1">
          <stop offset="0" stop-color="#c8408c"/>
          <stop offset="1" stop-color="#c43a87"/>
        </linearGradient>
        <linearGradient id="greenDisc" x1="0" y1="1" x2="1" y2="0">
          <stop offset="0" stop-color="#c6da2f"/>
          <stop offset="0.55" stop-color="#9cca3a"/>
          <stop offset="1" stop-color="#3db54a"/>
        </linearGradient>
        <linearGradient id="mistFade" x1="0" y1="0" x2="1" y2="0">
          <stop offset="0" stop-color="#5e5e5e" stop-opacity="0.85"/>
          <stop offset="0.7" stop-color="#3a3a3a" stop-opacity="0.5"/>
          <stop offset="1" stop-color="#231f20" stop-opacity="0"/>
        </linearGradient>
        <clipPath id="mugClip">
          <path d="M432 372 H1072 V798 A320 320 0 0 1 432 798 Z"/>
        </clipPath>
      </defs>

      <rect class="pattern-field" x="218" y="35" width="1066" height="1420" fill="url(#magentaField)" role="img" aria-label="Magenta background with swirling floral pattern"/>

      <circle class="accent-disc" cx="1250" cy="550" r="520" fill="url(#greenDisc)"/>

      <path class="mug-handle" d="M1088 518 H1150 A62 62 0 0 1 1212 580 V750 A62 62 0 0 1 1150 812 H1088 Z" fill="var(--ink)"/>
      <path class="mug-body" d="M432 372 H1072 V798 A320 320 0 0 1 432 798 Z" fill="var(--ink)"/>

      <rect class="mug-ornament" x="432" y="372" width="240" height="746" fill="url(#mistFade)" clip-path="url(#mugClip)" role="img" aria-label="Grey flowing leaf ornament along the left of the mug"/>
    </svg>

    <div class="brand-name">Brevo Leaf</div>
    <div class="tea-name">Tea Name</div>

    <div class="address-panel">
      <div class="address-brand">Brevo Leaf</div>
      <div class="address-line">846 Lower Maple Lane</div>
      <div class="address-line">Fernbrook, VT 05617</div>
    </div>

    <div class="field-label field-description">DESCRIPTION</div>
    <div class="field-label field-ingredients">INGREDIENTS</div>
  </div>
</div>
</body>
</html>
```